Business Card for Tutoring Company

We need a logo/symbol for an education company, along with an attractive business card. The logo should resemble both a pi symbol and the letter T.
Updates

Dear Designers,

I am narrowing down what I am looking for. 
I want the front of the card to be primarily white, with the company name "Bright Harbor Learning" positioned towards the center.  The first letter, 'T' in 'Bright' will be modified so that it resembles a Pi symbol.
My personal information will be at the bottom.  If you think it fits, the website can be strewn across the top.

As for the back of the card, it will be primarily blue.  Toward the center will be the same T/pi shape engraved into a circular disk/button/emblem shape with some border.  It should be noted that I do like shiny blue, like the blue face of a Varnel.  Underneath the logo will be white text that reads, "Making Independent Learners and Thinkers."  At the very bottom of the card in smaller white font, the website "BrightHarborLearning.example" is written.

For more clarification, see my recent attachment.

Thank you.

Leonard

Industry/Entity Type

Education

Logo styles of interest
Pictorial/Combination Logo
Requirements
Must have
• LOGO:
The logo is a solid blue circle with a symbol cutout from it. The cut out should closely resemble π and be the color white.

CARD:
The front has the logo in the top left corner, with "BRIGHT HARBOR LEARNING" written out beside it, spanning the width of the card. " At the bottom, personal information can be placed: Name, Title, Phone, Email.
The back has the the logo centered and enlarged. The website is printed "BrightHarborLearning.example
Nice to have
• LOGO:
It would be nice if the logo/pi symbol could be used as a letter T when spelling BHL or Bright Harbor Learning.

CARD:
The enlarged logo on the back of the card can be enhanced (i.e. the blue is not solid blue but shiny, like the metallic blue face of a varnel) It would also be nice if the logo had a cool background (i.e. instead of the cutout of the pi-shape being white, it could be outerspace or something. Also, a motto "Building Curious Learners and Thinkers" printed under "BrightHarborLearning.example" would be nice, if it fits.

```html
<!DOCTYPE html>
<html lang="en">
<head>
<meta charset="utf-8">
<title>Bright Harbor Learning – Business Card</title>
<link rel="stylesheet" href="https://fonts.googleapis.com/css2?family=Montserrat:wght@600;700&family=Open+Sans:wght@400;700&display=swap">
<style>
  :root {
    --stage: #3b3b3b;
    --navy: #1b237a;
    --blue-deep: #0b1a6b;
    --blue-mid: #12318f;
    --blue-shine: #2f5cc0;
    --white: #ffffff;
  }
  * { box-sizing: border-box; margin: 0; padding: 0; }
  html, body { width: 1200px; height: 900px; overflow: hidden; }
  body { background: var(--stage); position: relative; font-family: "Open Sans", sans-serif; }

  .card {
    position: absolute;
    top: 301px;
    width: 514px;
    height: 296px;
    overflow: hidden;
  }
  .shiny-blue {
    background:
      radial-gradient(ellipse 60% 80% at 78% 90%, rgba(47,92,192,.75), transparent 70%),
      radial-gradient(ellipse 45% 55% at 30% 25%, rgba(47,92,192,.55), transparent 70%),
      linear-gradient(120deg, var(--blue-mid) 0%, var(--blue-deep) 45%, var(--blue-mid) 75%, var(--blue-shine) 100%);
  }

  /* Back */
  .card-back { left: 72px; }
  .emblem {
    position: absolute;
    left: 50%; top: 43px;
    width: 154px; height: 154px;
    margin-left: -77px;
    border-radius: 50%;
    border: 2px solid var(--white);
    background: radial-gradient(circle at 40% 35%, var(--blue-shine), var(--blue-deep) 70%);
    display: flex; align-items: center; justify-content: center;
    text-align: center;
  }
  .emblem-name {
    font-family: "Montserrat", sans-serif;
    font-weight: 700;
    font-size: 17px;
    line-height: 1.2;
    color: var(--white);
  }
  .motto {
    position: absolute;
    left: 0; right: 0; top: 216px;
    text-align: center;
    font-family: "Montserrat", sans-serif;
    font-weight: 600;
    font-size: 15px;
    letter-spacing: 1.4px;
    line-height: 20px;
    color: var(--white);
  }
  .back-web {
    position: absolute;
    left: 0; right: 0; top: 266px;
    text-align: center;
    font-size: 14px;
    line-height: 18px;
    color: var(--white);
  }

  /* Front */
  .card-front { left: 615px; background: var(--white); }
  .top-band {
    position: absolute; left: 0; right: 0; top: 0; height: 40px;
    display: flex; align-items: center; justify-content: center;
    color: var(--white); font-size: 14px;
  }
  .wordmark {
    position: absolute; left: 0; right: 0; top: 60px;
    text-align: center;
    font-family: "Montserrat", sans-serif;
    font-weight: 700;
    color: var(--navy);
    line-height: 1;
  }
  .wordmark-main { display: block; font-size: 80px; letter-spacing: 1px; }
  .wordmark-sub { display: block; font-size: 27px; margin-top: 4px; letter-spacing: .3px; }
  .rule {
    position: absolute; left: 0; right: 0; top: 204px; height: 4px;
    background: var(--navy);
  }
  .contact-band {
    position: absolute; left: 0; right: 0; top: 213px; bottom: 0;
    color: var(--white);
  }
  .person { position: absolute; left: 49px; top: 14px; }
  .person-name { font-weight: 700; font-size: 18px; line-height: 1.3; }
  .person-title { font-size: 14px; line-height: 1.5; }
  .details { position: absolute; right: 48px; top: 15px; text-align: right; font-size: 14px; line-height: 1.55; }
</style>
</head>
<body>

  <section class="card card-back shiny-blue" aria-label="Card back">
    <div class="emblem">
      <span class="emblem-name">Bright Harbor<br>Learning</span>
    </div>
    <p class="motto">BUILDING CURIOUS LEARNERS AND THINKERS</p>
    <p class="back-web">BrightHarborLearning.example</p>
  </section>

  <section class="card card-front" aria-label="Card front">
    <div class="top-band shiny-blue">BrightHarborLearning.example</div>
    <h1 class="wordmark">
      <span class="wordmark-main">BRIGHT</span>
      <span class="wordmark-sub">HARBOR LEARNING</span>
    </h1>
    <div class="rule"></div>
    <div class="contact-band shiny-blue">
      <div class="person">
        <p class="person-name">Leonard Ashby</p>
        <p class="person-title">Education Consultant</p>
      </div>
      <div class="details">
        <p>(555) 014 2837</p>
        <p>leonard@BHLbest.example</p>
      </div>
    </div>
  </section>

</body>
</html>
```